Business Card Design Project

Business Card
We are rebranding with a new logo
Industry/Entity Type
Business
Contact Information for Business Card
Doug Farrow +61 457820913 doug@lumora.com.au P.O. Box 728 Kelmscott QLD 4309
Requirements
Must have
- Logo

```html
<!DOCTYPE html>
<html lang="en">
<head>
<meta charset="utf-8">
<title>Lumora International – Business Card</title>
<link href="https://fonts.googleapis.com/css2?family=Open+Sans:wght@400;600;700&display=swap" rel="stylesheet">
<style>
  :root {
    --page-bg: #3b3431;
    --card-bg: #161718;
    --card-edge: #202223;
    --brand-orange: #d9732a;
    --accent-blue: #2fa3d6;
    --text-light: #e9e9e9;
    --text-muted: #9a9a9a;
    --divider: #bdbdbd;
  }
  * { box-sizing: border-box; margin: 0; padding: 0; }
  html, body {
    width: 1200px; height: 864px; overflow: hidden;
    background: var(--page-bg);
    font-family: "Open Sans", Arial, sans-serif;
  }
  .sheet {
    width: 1200px; height: 864px;
    display: flex; align-items: center; justify-content: center; gap: 40px;
  }
  .card {
    width: 540px; height: 309px;
    background: linear-gradient(135deg, var(--card-edge), var(--card-bg) 60%);
    border-radius: 3px;
    box-shadow: 0 10px 30px rgba(0,0,0,.45);
    position: relative;
  }
  .brand-name {
    color: var(--brand-orange);
    font-weight: 700;
    letter-spacing: 3px;
    text-transform: uppercase;
    line-height: 1.15;
  }
  /* front */
  .card-front {
    display: flex; flex-direction: column; align-items: center; justify-content: center; gap: 44px;
  }
  .card-front .brand-name { font-size: 30px; text-align: center; }
  .website-spaced {
    color: var(--text-muted); font-size: 14px; letter-spacing: 6px;
  }
  /* back */
  .card-back {
    display: flex; align-items: center; padding: 0 36px 0 40px;
  }
  .card-back .brand-block { width: 230px; }
  .card-back .brand-name { font-size: 24px; }
  .divider {
    width: 1px; height: 150px; margin: 0 24px;
    background: linear-gradient(to bottom, transparent, var(--divider), transparent);
  }
  .contact { color: var(--text-light); font-size: 15px; line-height: 1.45; }
  .contact-name {
    color: var(--accent-blue); font-weight: 700; font-size: 16px;
    text-transform: uppercase; margin-bottom: 10px; letter-spacing: .5px;
  }
  .contact-line { display: flex; align-items: center; gap: 8px; }
  .contact-line svg { width: 12px; height: 12px; fill: var(--accent-blue); flex: none; }
  .address { margin-bottom: 2px; }
</style>
</head>
<body>
<main class="sheet">
  <section class="card card-front">
    <div class="brand-name">Lumora<br>International</div>
    <div class="website-spaced">www.lumora.com.au</div>
  </section>

  <section class="card card-back">
    <div class="brand-block">
      <div class="brand-name">Lumora<br>International</div>
    </div>
    <div class="divider"></div>
    <div class="contact">
      <div class="contact-name">Doug Farrow</div>
      <div class="address">P.O. Box 728<br>Kelmscott QLD 4309</div>
      <div class="contact-line">
        <svg viewBox="0 0 24 24" aria-hidden="true"><path d="M6.6 10.8a15 15 0 0 0 6.6 6.6l2.2-2.2c.3-.3.7-.4 1-.2 1.1.4 2.3.6 3.6.6.6 0 1 .4 1 1V20c0 .6-.4 1-1 1A17 17 0 0 1 3 4c0-.6.4-1 1-1h3.5c.6 0 1 .4 1 1 0 1.3.2 2.5.6 3.6.1.3 0 .7-.2 1z"/></svg>
        <span>+61 457820913</span>
      </div>
      <div class="contact-line">
        <svg viewBox="0 0 24 24" aria-hidden="true"><path d="M2 5h20v14H2zm2 2v.5l8 5 8-5V7l-8 5z"/></svg>
        <span>doug@lumora.com.au</span>
      </div>
      <div class="contact-line">
        <svg viewBox="0 0 24 24" aria-hidden="true"><path d="M12 2a10 10 0 1 0 0 20 10 10 0 0 0 0-20zm6.9 9h-3a15 15 0 0 0-1.3-6A8 8 0 0 1 18.9 11zM12 4c.9 1.2 1.7 3.7 1.9 7h-3.8C10.3 7.7 11.1 5.2 12 4zM9.4 5a15 15 0 0 0-1.3 6h-3A8 8 0 0 1 9.4 5zM5.1 13h3a15 15 0 0 0 1.3 6A8 8 0 0 1 5.1 13zM12 20c-.9-1.2-1.7-3.7-1.9-7h3.8c-.2 3.3-1 5.8-1.9 7zm2.6-1a15 15 0 0 0 1.3-6h3a8 8 0 0 1-4.3 6z"/></svg>
        <span>www.lumora.com.au</span>
      </div>
    </div>
  </section>
</main>
</body>
</html>
```